Bolt haven latch

We have created A revolutionary new design for door chains offering incredible strength and simplicity of instillation. Our product is called the Bolt Haven Latch. We are seeking a web site to promote and sell our lock. We want to promote that this lock is simple to install and much stronger than existing lock. www.ferrowardlatches.example We are in the process of making a third video to replace the current one.. The first video is also on YouTube under toughest entry guard early model demo.

Target Market(s)

homeowners, apartments, dorm rooms, our someone wanting to turn a bedroom into a safe room ( somewhere they can go to in an emergency such as a break in).

Industry/Entity Type

Product

Font styles to use
Sans Serif

Requirements
Must have
• A video showing are product the weakness of existing door chains and the strength of are lock. A location where they can purchase our lock.
Nice to have
• A quick bio of the inventor of the lock a police officer for 22 years, retired but still concerned about safety and security

```html
<!DOCTYPE html>
<html lang="en">
<head>
<meta charset="utf-8">
<title>Bolt Haven Latch</title>
<link href="https://fonts.googleapis.com/css2?family=Roboto:wght@300;400;500;700&display=swap" rel="stylesheet">
<style>
:root{
  --brand-blue:#2a80fb;
  --brand-blue-dark:#1f6fe0;
  --ink:#2f2f2f;
  --body-text:#4a4a4a;
  --band-bg:#e5e5e5;
  --footer-bg:#000;
  --footer-text:#c9c9c9;
  --white:#fff;
}
*{box-sizing:border-box;margin:0;padding:0}
html,body{width:1200px;height:1016px;overflow:hidden}
body{font-family:'Roboto',sans-serif;background:var(--band-bg);position:relative;color:var(--ink)}

.site-header{position:absolute;left:0;top:0;width:1200px;height:139px;background:var(--brand-blue)}
.brand{position:absolute;left:172px;top:28px;display:flex;align-items:center;gap:10px;color:var(--white);font-weight:700;font-size:24px;letter-spacing:.3px}
.brand-mark{width:22px;height:22px;border-radius:50%;background:var(--white)}
.header-phone{position:absolute;right:172px;top:33px;display:flex;align-items:center;gap:10px;color:var(--white);font-size:20px;font-weight:300}
.header-phone svg{width:36px;height:36px}
.main-nav{position:absolute;left:403px;top:88px;width:625px;height:51px}
.nav-item{position:absolute;top:0;height:51px;line-height:51px;color:var(--white);font-size:14px;text-decoration:none;text-align:center}
.nav-item.is-active{background:#000;border-radius:26px 26px 0 0;width:85px;left:0}
.nav-divider{position:absolute;top:16px;width:1px;height:26px;background:rgba(255,255,255,.5)}
.header-rule{position:absolute;left:172px;top:139px;width:856px;height:6px;background:linear-gradient(rgba(0,0,0,.35),rgba(0,0,0,0));border-radius:50%}

.hero-video{position:absolute;left:0;top:139px;width:1200px;height:428px;background:radial-gradient(ellipse at 55% 55%,#8a8577 0%,#b9b6ae 35%,#c9c9c7 60%,#bdbdbb 100%)}
.play-button{position:absolute;left:534px;top:155px;width:100px;height:100px;border-radius:50%;background:var(--brand-blue);box-shadow:0 2px 8px rgba(0,0,0,.2)}
.play-button svg{position:absolute;left:0;top:0;width:100px;height:100px}
.play-label{position:absolute;left:0;width:1200px;top:268px;text-align:center;color:var(--white);font-weight:500;font-size:24px;text-shadow:0 1px 3px rgba(0,0,0,.35)}

.tagline{position:absolute;left:172px;top:591px;width:856px;text-align:center;font-weight:300;font-size:30px;line-height:38px;white-space:nowrap;color:#333}
.feature{position:absolute;top:656px;width:264px}
.feature h2{font-size:15px;font-weight:500;color:#333;margin-bottom:13px;height:19px;white-space:nowrap}
.feature p{font-size:12px;font-weight:300;line-height:17px;color:var(--body-text)}
.feature--welcome{left:173px}
.feature--benefits{left:470px}
.feature--bio{left:764px}
.benefit-list{list-style:none}
.benefit-list li{position:relative;padding-left:17px;font-size:12px;line-height:16px;color:var(--body-text);margin-bottom:8px}
.benefit-list svg{position:absolute;left:0;top:3px;width:13px;height:12px}
.bio-text{height:133px;overflow:hidden}
.bio-text p{line-height:19px}
.bio-photo{float:right;width:94px;height:103px;margin:3px 0 4px 12px;background:linear-gradient(160deg,#3a4a63,#8a7a5c 60%,#b49a72)}
.btn-more{position:absolute;top:844px;height:33px;width:89px;background:var(--brand-blue);border-radius:2px;color:var(--white);font-size:12px;font-weight:500;display:flex;align-items:center;justify-content:center;gap:5px;text-decoration:none}
.btn-more svg{width:11px;height:11px}

.site-footer{position:absolute;left:0;top:915px;width:1200px;height:101px;background:var(--footer-bg)}
.footer-emblem{position:absolute;left:531px;top:0;width:130px;height:78px;border-radius:0 0 65px 65px;background:#161616}
.social{position:absolute;left:542px;top:35px;display:flex;gap:20px}
.social span{width:14px;height:14px;border-radius:50%;background:#ddd;display:block}
.footer-copy{position:absolute;left:173px;top:58px;font-size:11px;font-weight:300;color:var(--footer-text)}
.footer-contact{position:absolute;right:175px;top:59px;font-size:11px;font-weight:300;color:var(--footer-text)}
</style>
</head>
<body>
<header class="site-header">
  <div class="brand"><span class="brand-mark"></span>Bolt Haven Latch</div>
  <div class="header-phone">
    <svg viewBox="0 0 36 36"><circle cx="18" cy="18" r="17" fill="none" stroke="#0b2a55" stroke-width="1.3"/><path d="M13.5 11.5c1-.7 1.8-.6 2.4.4l1 1.8c.4.8.2 1.4-.5 1.9l-.8.5c.6 1.8 1.8 3.2 3.4 4.1l.6-.7c.6-.6 1.2-.7 1.9-.2l1.7 1.2c.8.6.9 1.4.1 2.300-1 1.1-2.4 1.4-3.9.7-3.6-1.6-6.3-4.6-7.3-8.3-.3-1.4.3-2.9 1.4-3.7z" fill="#fff"/></svg>
    555-0142-7788
  </div>
  <nav class="main-nav">
    <a class="nav-item is-active" href="#">Home</a>
    <a class="nav-item" style="left:134px;width:80px" href="#">About Us</a>
    <span class="nav-divider" style="left:246px"></span>
    <a class="nav-item" style="left:277px;width:80px" href="#">Services</a>
    <span class="nav-divider" style="left:377px"></span>
    <a class="nav-item" style="left:418px;width:60px" href="#">Blogs</a>
    <span class="nav-divider" style="left:509px"></span>
    <a class="nav-item" style="left:545px;width:80px;text-align:right" href="#">Contact Us</a>
  </nav>
</header>
<div class="header-rule"></div>

<section class="hero-video" role="img" aria-label="Video still: door lever handle with a brass door chain latch fitted to a white door frame">
  <div class="play-button"><svg viewBox="0 0 100 100"><path d="M37 29v42l34-21z" fill="#fff"/></svg></div>
  <div class="play-label">CLICK HERE TO PLAY VIDEO</div>
</section>

<h1 class="tagline">there is nothing else on the market equal to bolt haven latches</h1>

<section class="feature feature--welcome">
  <h2>WELCOME TO BOLT HAVEN LATCH</h2>
  <p>Nunc eros justo, porttitor non nulla tempus, egestas blandit massa. Quisque sit amet dictum ante, tincidunt ultricies urna. Sed sed est ut dui commodo dignissim. Nunc dapibus erat id porttitor sodales. Aliquam nec neque a massa condimentum fermentum id eget ante. Fusce nec nulla nec tortor blandit scelerisque ut nec magna. Nulla vitae malesuada nunc, eu sagittis lorem.</p>
</section>

<section class="feature feature--benefits">
  <h2>Bolt Haven Benefits</h2>
  <ul class="benefit-list">
    <li><svg viewBox="0 0 13 12"><rect x=".7" y="2.7" width="9" height="8.6" rx="1" fill="none" stroke="#2a80fb" stroke-width="1.3"/><path d="M3 6l2.3 2.3L12 1.5" fill="none" stroke="#2a80fb" stroke-width="1.8"/></svg>Added safety and security , dual locks</li>
    <li><svg viewBox="0 0 13 12"><rect x=".7" y="2.7" width="9" height="8.6" rx="1" fill="none" stroke="#2a80fb" stroke-width="1.3"/><path d="M3 6l2.3 2.3L12 1.5" fill="none" stroke="#2a80fb" stroke-width="1.8"/></svg>Stronger lock because of placement of lock</li>
    <li><svg viewBox="0 0 13 12"><rect x=".7" y="2.7" width="9" height="8.6" rx="1" fill="none" stroke="#2a80fb" stroke-width="1.3"/><path d="M3 6l2.3 2.3L12 1.5" fill="none" stroke="#2a80fb" stroke-width="1.8"/></svg>screws are longer than screw on current door chains</li>
    <li><svg viewBox="0 0 13 12"><rect x=".7" y="2.7" width="9" height="8.6" rx="1" fill="none" stroke="#2a80fb" stroke-width="1.3"/><path d="M3 6l2.3 2.3L12 1.5" fill="none" stroke="#2a80fb" stroke-width="1.8"/></svg>Better placement of screws</li>
    <li><svg viewBox="0 0 13 12"><rect x=".7" y="2.7" width="9" height="8.6" rx="1" fill="none" stroke="#2a80fb" stroke-width="1.3"/><path d="M3 6l2.3 2.3L12 1.5" fill="none" stroke="#2a80fb" stroke-width="1.8"/></svg>Useable on all types of doors, wood, metal</li>
    <li><svg viewBox="0 0 13 12"><rect x=".7" y="2.7" width="9" height="8.6" rx="1" fill="none" stroke="#2a80fb" stroke-width="1.3"/><path d="M3 6l2.3 2.3L12 1.5" fill="none" stroke="#2a80fb" stroke-width="1.8"/></svg>Ease of installation</li>
  </ul>
</section>

<section class="feature feature--bio">
  <h2>BIO OF THE INVENTOR</h2>
  <div class="bio-text">
    <div class="bio-photo" role="img" aria-label="Portrait photo of the inventor in a sheriff's uniform"></div>
    <p>I retired from the Harbor Valley county sheriff's department as a deputy sheriff after 22 years of service, because of a back injury. In February 2014. I suffered a major relapse with my back and was in the hospital for two weeks. I after the hospital I went home and started thinking about safety.</p>
  </div>
</section>

<a class="btn-more" style="left:349px" href="#">View more <svg viewBox="0 0 12 12"><circle cx="6" cy="6" r="6" fill="#fff"/><path d="M3 6h5M6 3.6L8.4 6 6 8.4" fill="none" stroke="#2a80fb" stroke-width="1.6"/></svg></a>
<a class="btn-more" style="left:645px" href="#">View more <svg viewBox="0 0 12 12"><circle cx="6" cy="6" r="6" fill="#fff"/><path d="M3 6h5M6 3.6L8.4 6 6 8.4" fill="none" stroke="#2a80fb" stroke-width="1.6"/></svg></a>
<a class="btn-more" style="left:939px" href="#">View more <svg viewBox="0 0 12 12"><circle cx="6" cy="6" r="6" fill="#fff"/><path d="M3 6h5M6 3.6L8.4 6 6 8.4" fill="none" stroke="#2a80fb" stroke-width="1.6"/></svg></a>

<footer class="site-footer">
  <div class="footer-emblem"></div>
  <div class="social" aria-label="Social links"><span></span><span></span><span></span><span></span></div>
  <p class="footer-copy">Copyright © 2014 - All rights reserved. Terms &amp; Condition &nbsp;|&nbsp; Privacy policy</p>
  <p class="footer-contact">18 Maple Hollow Road Brookfield, 555-0142-7788 &nbsp;|&nbsp; info@ferrowardlatches.example</p>
</footer>
</body>
</html>
```